BoldPickleHop417

I want to create a website that will have fun design. The subject is the crazy drivers in Miami. I want to show a cool logo, a top banner on the website that is a video background.

And then below I would like to have advertisements, and then a collection of video, article, and image divs shown that can be clicked on. Each page opened will have advertising or affiliate marketing links.

```html
<!DOCTYPE html>
<html lang="en">
<head>
<meta charset="utf-8">
<title>BoldPickleHop417</title>
<link href="https://fonts.googleapis.com/css2?family=Bungee&family=Montserrat:wght@500&family=Roboto:wght@400;700&display=swap" rel="stylesheet">
<style>
  :root {
    --backdrop: #737373;
    --nav-bg: #1b1b1b;
    --page-bg: #1f1f1f;
    --band-bg: #232323;
    --card-bg: #1a1a1a;
    --hero-start: #18cb94;
    --hero-end: #9cc230;
    --title-yellow: #ffe41a;
    --sub-ink: #2a1830;
    --pink: #ff1f8f;
    --text-light: #e2e2e2;
    --white: #ffffff;
  }
  * { box-sizing: border-box; margin: 0; padding: 0; }
  html, body { width: 1200px; height: 714px; overflow: hidden; background: var(--backdrop); }
  .site {
    position: absolute; left: 64px; top: 47px; width: 1071px; height: 619px;
    background: var(--page-bg); box-shadow: 0 6px 24px rgba(0,0,0,.35);
    font-family: "Roboto", sans-serif;
  }
  .topbar {
    position: absolute; left: 0; top: 0; width: 100%; height: 31px;
    background: var(--nav-bg); z-index: 2;
  }
  .brand {
    position: absolute; left: 10px; top: 9px; display: flex; align-items: center; gap: 5px;
    font-family: "Roboto", sans-serif; font-weight: 700; font-size: 13px; color: var(--white);
  }
  .brand-dot { width: 12px; height: 12px; border-radius: 50%; background: var(--pink); }
  .main-nav {
    position: absolute; left: 515px; top: 8px; display: flex; gap: 11px;
    font-family: "Bungee", sans-serif; font-size: 9.5px; letter-spacing: .2px;
  }
  .main-nav a { color: var(--white); text-decoration: none; }
  .menu-toggle {
    position: absolute; right: 11px; top: 12px; width: 6px; height: 6px;
    display: flex; flex-direction: column; justify-content: space-between;
  }
  .menu-toggle span { display: block; height: 1px; background: var(--white); }
  .hero {
    position: absolute; left: 0; top: 31px; width: 100%; height: 372px;
    background: linear-gradient(to top right, var(--hero-start), #55c563 55%, var(--hero-end));
    text-align: center;
  }
  .hero-title {
    position: absolute; left: 0; width: 100%; top: 155px;
    font-family: "Bungee", sans-serif; font-weight: 400; font-size: 36px; line-height: 1;
    color: var(--title-yellow); text-shadow: 2px 3px 4px rgba(0,0,0,.4);
  }
  .hero-tagline {
    position: absolute; left: 0; width: 100%; top: 196px;
    font-family: "Montserrat", sans-serif; font-weight: 500; font-size: 10.5px; color: var(--sub-ink);
  }
  .ad-band { position: absolute; left: 0; top: 403px; width: 100%; height: 23px; background: var(--band-bg); }
  .collection {
    position: absolute; left: 11px; top: 437px; display: flex; gap: 11px;
  }
  .tile {
    width: 342px; height: 138px; background: var(--card-bg); border-radius: 4px; overflow: hidden;
  }
  .tile-media { height: 83px; }
  .media-purple { background: linear-gradient(100deg, #5a2a7a, #b7462c 30%, #6e3a9a 55%, #3c5a7a 80%, #7a3a9a); }
  .media-panels { background: linear-gradient(180deg, #3a2a48 0%, #3a4a8a 35%, #8a3a3a 60%, #4a5a7a 100%); }
  .tile-title {
    margin: 12px 0 0 8px; font-weight: 700; font-size: 10.5px; color: var(--pink);
  }
  .tile-text { margin: 8px 0 0 8px; font-size: 8px; color: var(--text-light); }
  .site-footer {
    position: absolute; left: 0; bottom: 0; width: 100%; height: 33px;
    background: var(--nav-bg); text-align: center; color: var(--text-light);
  }
  .copyright { font-size: 7.2px; margin-top: 9px; }
  .disclosure { font-size: 5.8px; margin-top: 3px; }
</style>
</head>
<body>
<div class="site">
  <header class="topbar">
    <div class="brand"><span class="brand-dot"></span>BoldPickleHop417</div>
    <nav class="main-nav">
      <a href="#">Home</a><a href="#">Videos</a><a href="#">Articles</a><a href="#">Gallery</a>
    </nav>
    <div class="menu-toggle"><span></span><span></span><span></span></div>
  </header>

  <section class="hero">
    <h1 class="hero-title">BOLDPICKLEHOP417</h1>
    <p class="hero-tagline">A wild ride through Miami's craziest streets.</p>
  </section>

  <div class="ad-band"></div>

  <section class="collection">
    <article class="tile">
      <div class="tile-media media-purple" role="img" aria-label="Banner illustration of wild videos, crazy articles and insane photos of Miami driving"></div>
      <h2 class="tile-title">Dash Cam Chaos</h2>
      <p class="tile-text">A compilation of the craziest drivers on Miami roads.</p>
    </article>
    <article class="tile">
      <div class="tile-media media-panels" role="img" aria-label="Panel illustration of crazy videos, wild articles and WTF photos with ad buttons"></div>
      <h2 class="tile-title">Drivers Gone Wild</h2>
      <p class="tile-text">Find out why Miami’s traffic is unlike anywhere else.</p>
    </article>
    <article class="tile">
      <div class="tile-media media-panels" role="img" aria-label="Panel illustration of crazy videos, wild articles and WTF photos with ad buttons"></div>
      <h2 class="tile-title">Photo Fails</h2>
      <p class="tile-text">Outrageous parking jobs and crazy car photos.</p>
    </article>
  </section>

  <footer class="site-footer">
    <p class="copyright">© 2026 BoldPickleHop417. All rights reserved.</p>
    <p class="disclosure">Some links on this site may be affiliate links that help support our work.</p>
  </footer>
</div>
</body>
</html>
```